Business Card Design

I already have a company logo for my company. I have a logo for the manufacturer we represent. I want a professional business card design.

```html
<!DOCTYPE html>
<html lang="en">
<head>
<meta charset="utf-8">
<title>Beacon Hazard Services – Business Card</title>
<link href="https://fonts.googleapis.com/css2?family=Lato:wght@400;700;900&family=Michroma&display=swap" rel="stylesheet">
<style>
  :root{
    --page:#d9d9db;
    --card:#222224;
    --card-light:#2e2e31;
    --edge:#e3a715;
    --red:#e3262b;
    --gold:#e6a81a;
    --silver:#e9e9ea;
    --text:#f2f2f2;
  }
  *{box-sizing:border-box;margin:0;padding:0}
  html,body{width:1200px;height:982px;overflow:hidden}
  body{background:var(--page);font-family:'Lato',sans-serif;position:relative}
  .card{
    position:absolute;left:250px;width:700px;height:400px;border-radius:22px;
    background:radial-gradient(ellipse at 40% 35%,var(--card-light),var(--card) 75%);
    border-bottom:4px solid var(--edge);
    box-shadow:0 14px 30px rgba(0,0,0,.35);
    overflow:hidden;
  }
  .card--front{top:70px}
  .card--back{top:512px}
  .brand{display:flex;align-items:center;gap:14px;color:var(--silver);font-weight:900;letter-spacing:1px;line-height:1}
  .brand__mark{width:20px;height:20px;background:var(--red);flex:none}
  .card--front .brand{position:absolute;left:0;right:0;top:170px;justify-content:center;font-size:40px}
  .card--back .brand{position:absolute;left:40px;top:180px;font-size:25px;width:240px;flex-wrap:nowrap}
  .divider{position:absolute;left:298px;top:60px;width:2px;height:290px;
    background:linear-gradient(to bottom,transparent,#f5f5f5 40%,#9a9a9a 80%,transparent)}
  .contact{position:absolute;left:330px;top:52px;width:350px;color:var(--text)}
  .contact__name{font-family:'Michroma',sans-serif;color:var(--red);font-size:30px;letter-spacing:2px;line-height:1.1}
  .contact__role{color:var(--gold);font-size:19px;margin:6px 0 22px}
  .contact__list{list-style:none}
  .contact__item{display:flex;align-items:flex-start;gap:12px;font-size:18px;line-height:1.3;margin-bottom:5px}
  .contact__item svg{width:16px;height:16px;flex:none;margin-top:3px;fill:var(--red)}
</style>
</head>
<body>
  <section class="card card--front" aria-label="Card front">
    <div class="brand"><span class="brand__mark"></span>BEACON HAZARD SERVICES LLC</div>
  </section>

  <section class="card card--back" aria-label="Card back">
    <div class="brand"><span class="brand__mark"></span>BEACON HAZARD</div>
    <div class="divider"></div>
    <div class="contact">
      <h1 class="contact__name">DANIEL REYES</h1>
      <p class="contact__role">Founder &amp; CEO</p>
      <ul class="contact__list">
        <li class="contact__item"><svg viewBox="0 0 16 16"><path d="M8 0a6 6 0 0 0-6 6c0 4.5 6 10 6 10s6-5.5 6-10a6 6 0 0 0-6-6zm0 8.5A2.5 2.5 0 1 1 8 3.5a2.5 2.5 0 0 1 0 5z"/></svg><span>78 Harbor Lane, Fairview<br>OH 44102 USA</span></li>
        <li class="contact__item"><svg viewBox="0 0 16 16"><path d="M3.5 1l2.5 3-1.5 2c1 2 2.5 3.5 4.5 4.5l2-1.5 3 2.5-1.5 3C7 14 2 9 1 2.5z"/></svg><span>(555) 014-2290</span></li>
        <li class="contact__item"><svg viewBox="0 0 16 16"><path d="M4 0h8a1 1 0 0 1 1 1v14a1 1 0 0 1-1 1H4a1 1 0 0 1-1-1V1a1 1 0 0 1 1-1zm1 2v10h6V2zm3 11a1 1 0 1 0 0 2 1 1 0 0 0 0-2z"/></svg><span>(555) 014-2291</span></li>
        <li class="contact__item"><svg viewBox="0 0 16 16"><path d="M4 0h8v4H4zM1 5h14v7h-3v4H4v-4H1zm4 5v5h6v-5z"/></svg><span>(555) 014-2292</span></li>
        <li class="contact__item"><svg viewBox="0 0 16 16"><path d="M0 3h16v1L8 9 0 4zm0 3l8 5 8-5v8H0z"/></svg><span>info@beaconhazard.com</span></li>
        <li class="contact__item"><svg viewBox="0 0 16 16"><path d="M8 0a8 8 0 1 0 0 16A8 8 0 0 0 8 0zm0 1.5c1 1.2 1.7 3 1.9 5.5H6.1C6.3 4.5 7 2.7 8 1.5zM1.6 9h3c.2 2 .7 3.6 1.4 4.8A6.5 6.5 0 0 1 1.6 9zm4.5 0h3.8c-.2 2.4-.9 4.2-1.9 5.5-1-1.3-1.7-3.1-1.9-5.5zm5.3 0h3a6.5 6.5 0 0 1-4.4 4.8c.7-1.2 1.2-2.8 1.4-4.8zM1.6 7A6.5 6.5 0 0 1 6 2.2C5.3 3.4 4.8 5 4.6 7zm9.8 0c-.2-2-.7-3.6-1.4-4.8A6.5 6.5 0 0 1 14.4 7z"/></svg><span>beaconhazard.com</span></li>
      </ul>
    </div>
  </section>
</body>
</html>
```